Chiropractic Auto Accident Billboard

Billboard for Auto Accident Chiropractor
Kestrelwood Rehab
(770) 48-SPINE
Habla Espanol
Same Day Appointments - Locations across Georgia
INJURED IN A CAR ACCIDENT?

Target Market(s)

People in Auto Accidents

Industry/Entity Type

Personal Injury

Requirements
Must have
• BIG PHONE Number

```html
<!DOCTYPE html>
<html lang="en">
<head>
<meta charset="utf-8">
<title>Kestrelwood Rehab – Auto Injury Billboard</title>
<link href="https://fonts.googleapis.com/css2?family=Montserrat:wght@600;700;800&display=swap" rel="stylesheet">
<style>
  :root {
    --page: #e9edf1;
    --board: #161616;
    --portrait-top: #24435c;
    --portrait-bottom: #15293a;
    --green: #6cb047;
    --green-light: #82c45c;
    --green-dark: #4f8f35;
    --headline-green: #78b852;
    --white: #ffffff;
  }
  * { margin: 0; padding: 0; box-sizing: border-box; }
  html, body {
    width: 1200px; height: 532px; overflow: hidden;
    background: var(--page);
    font-family: "Montserrat", sans-serif;
  }
  .billboard {
    position: absolute; left: 0; top: 76px;
    width: 1200px; height: 380px;
    background: var(--board);
    overflow: hidden;
  }
  .phone-band {
    position: absolute; left: 330px; top: 163px;
    width: 870px; height: 110px;
    background: linear-gradient(90deg, var(--green-dark) 0%, var(--green-light) 45%, var(--green) 100%);
  }
  .portrait-panel {
    position: absolute; left: 0; top: 0;
    width: 370px; height: 380px;
  }
  .headline {
    position: absolute; left: 382px; top: 30px;
    font-weight: 800; font-size: 53px; line-height: 59px;
    letter-spacing: 1px; color: var(--white);
  }
  .headline .accent { display: block; color: var(--headline-green); }
  .headline .lead { display: block; font-weight: 700; letter-spacing: 3px; }
  .brand {
    position: absolute; left: 930px; top: 92px;
    display: flex; align-items: center; gap: 8px;
  }
  .brand-dot {
    width: 22px; height: 22px; border-radius: 50%;
    background: var(--green);
  }
  .brand-name {
    font-weight: 700; font-size: 22px; color: var(--headline-green);
    white-space: nowrap;
  }
  .phone-number {
    position: absolute; left: 372px; top: 163px;
    width: 812px; height: 110px;
  }
  .phone-number text {
    font-family: "Montserrat", sans-serif;
    font-weight: 800; font-size: 102px; fill: var(--white);
  }
  .details {
    position: absolute; left: 382px; top: 290px; width: 800px;
    text-align: center; color: var(--white);
  }
  .details .availability { font-weight: 700; font-size: 26px; line-height: 32px; }
  .details .language {
    margin-top: 8px; font-weight: 600; font-size: 24px;
    letter-spacing: 1px; color: var(--headline-green);
  }
</style>
</head>
<body>
  <main class="billboard">
    <div class="phone-band"></div>

    <svg class="portrait-panel" viewBox="0 0 370 380" role="img" aria-label="Portrait photo of the smiling chiropractor in a dark blazer">
      <defs>
        <linearGradient id="portraitFill" x1="0" y1="0" x2="0" y2="1">
          <stop offset="0" stop-color="var(--portrait-top)"/>
          <stop offset="1" stop-color="var(--portrait-bottom)"/>
        </linearGradient>
      </defs>
      <path d="M0 0 H318 C345 60 358 130 352 190 C346 260 320 330 296 380 H0 Z" fill="url(#portraitFill)"/>
      <path d="M318 0 C345 60 358 130 352 190 C346 260 320 330 296 380" fill="none" stroke="var(--green)" stroke-width="9"/>
    </svg>

    <h1 class="headline">
      <span class="lead">INJURED IN A</span>
      <span class="accent">CAR ACCIDENT?</span>
    </h1>

    <div class="brand">
      <span class="brand-dot"></span>
      <span class="brand-name">Kestrelwood Rehab</span>
    </div>

    <svg class="phone-number" viewBox="0 0 812 110" aria-label="(770) 48-SPINE">
      <text x="2" y="93" textLength="806" lengthAdjust="spacingAndGlyphs">(770) 48-SPINE</text>
    </svg>

    <div class="details">
      <p class="availability">Same Day Appointments - Locations across Georgia</p>
      <p class="language">HABLA ESPANOL</p>
    </div>
  </main>
</body>
</html>
```